Tall Oak Circle.. a non profit that seeks to stomp out skin cancer .. smalls steps toward making big

Simple letterhead incorporating logo

Industry/Entity Type

Non Profit

Font styles to use
Sans Serif

Colors

Designer to choose colors to be used in the design.

```html
<!DOCTYPE html>
<html lang="en">
<head>
<meta charset="utf-8">
<title>Tall Oak Circle — Letterhead</title>
<link href="https://fonts.googleapis.com/css2?family=Source+Sans+3:wght@400;700&display=swap" rel="stylesheet">
<style>
  :root {
    --backdrop: #e9e7e4;
    --paper: #ffffff;
    --brand-yellow: #f7dc00;
    --brand-ink: #23232b;
    --rule-navy: #1f2233;
  }
  * { box-sizing: border-box; margin: 0; padding: 0; }
  html, body {
    width: 1200px;
    height: 900px;
    overflow: hidden;
    background: var(--backdrop);
    font-family: "Source Sans 3", sans-serif;
  }
  .canvas {
    position: relative;
    width: 1200px;
    height: 900px;
  }
  .letterhead {
    position: absolute;
    left: 323px;
    top: 33px;
    width: 554px;
    height: 834px;
    background: var(--paper);
    box-shadow: 0 4px 18px rgba(0, 0, 0, 0.12);
    overflow: hidden;
  }
  .corner-trim {
    position: absolute;
    inset: 0;
    width: 554px;
    height: 834px;
  }
  .brand {
    position: absolute;
    right: 44px;
    top: 98px;
    display: flex;
    align-items: center;
    gap: 10px;
  }
  .brand-name {
    font-size: 22px;
    font-weight: 700;
    color: var(--brand-ink);
    letter-spacing: 0.2px;
  }
  .brand-dot {
    width: 30px;
    height: 30px;
    border-radius: 50%;
    background: var(--brand-yellow);
  }
  .contact-rule {
    position: absolute;
    left: 116px;
    top: 201px;
    width: 3px;
    height: 469px;
    background: var(--rule-navy);
  }
  .contact-list {
    position: absolute;
    left: 15px;
    top: 0;
    width: 80px;
    list-style: none;
  }
  .contact-item {
    position: absolute;
    left: 0;
    width: 80px;
    display: flex;
    flex-direction: column;
    align-items: center;
  }
  .contact-icon {
    width: 24px;
    height: 24px;
    fill: var(--brand-yellow);
  }
  .contact-label {
    margin-top: 14px;
    font-size: 15px;
    font-weight: 700;
    color: var(--rule-navy);
    letter-spacing: -0.2px;
  }
  .contact-phone   { top: 216px; }
  .contact-fax     { top: 302px; }
  .contact-email   { top: 399px; }
  .contact-website { top: 502px; }
</style>
</head>
<body>
<main class="canvas">
  <article class="letterhead">
    <svg class="corner-trim" viewBox="0 0 554 834" aria-hidden="true">
      <polygon points="0,0 554,0 554,18 80,18 0,81" fill="var(--brand-yellow)"/>
      <polygon points="0,0 66,0 0,58" fill="var(--brand-ink)"/>
      <polygon points="0,816 466,816 554,742 554,834 0,834" fill="var(--brand-yellow)"/>
      <polygon points="554,766 554,834 474,834" fill="var(--brand-ink)"/>
    </svg>

    <header class="brand">
      <span class="brand-name">Tall Oak Circle</span>
      <span class="brand-dot"></span>
    </header>

    <ul class="contact-list">
      <li class="contact-item contact-phone">
        <svg class="contact-icon" viewBox="0 0 24 24" aria-hidden="true">
          <path d="M8 2h6v5h-4v10h4v5H8c-1.7 0-3-1.3-3-3V5c0-1.7 1.3-3 3-3z" transform="translate(24 0) scale(-1 1)"/>
        </svg>
        <span class="contact-label">PHONE</span>
      </li>
      <li class="contact-item contact-fax">
        <svg class="contact-icon" viewBox="0 0 24 24" aria-hidden="true">
          <path d="M7 3h10v6H7zM4 10h16v7h-3v-3H7v3H4zM8 15h8v6H8zM9 16.5v1h6v-1zM9 18.5v1h6v-1z"/>
        </svg>
        <span class="contact-label">FAX</span>
      </li>
      <li class="contact-item contact-email">
        <svg class="contact-icon" viewBox="0 0 24 24" aria-hidden="true">
          <path d="M2 5h20v14H2zm2 2v.4l8 6 8-6V7zm0 2.9V17h16V9.9l-8 6z"/>
        </svg>
        <span class="contact-label">EMAIL</span>
      </li>
      <li class="contact-item contact-website">
        <svg class="contact-icon" viewBox="0 0 24 24" aria-hidden="true">
          <path d="M12 2a10 10 0 1 0 0 20 10 10 0 0 0 0-20zm-2 3c1 1 0 2 1 3s2 0 2 2-2 1-3 2-1 3-3 3-2-3-3-4c0-3 2-5 6-6zm6 6c2 0 3 1 3 3-1 3-3 5-6 5 0-2 1-3 1-4s-1-2 0-3 1-1 2-1z"/>
        </svg>
        <span class="contact-label">WEBSITE</span>
      </li>
    </ul>

    <div class="contact-rule"></div>
  </article>
</main>
</body>
</html>
```